MBW Website

I'm looking to design a 1 page website for my email marketing business called 'Inbox Harvest Works.' The business will be designed to attract eCommerce clients in particular.

It will be a very simple website with my picture, a Subscribe area to capture email addresses (and send out lead magnet PDFs), and some basic copy and social media links, nothing fancy!

I will provide the profile picture and all related copy, looking to use the color green and have it fill up the entire screen.

Here's an example of a similar site I really like:

http://prosecraftacademy-example.com/

I'm just looking for the site to provide information about my email marketing services and make a personal connection with the site visitors.

Target Market(s)

eCommerce businesse customers

Industry/Entity Type

Business

Number of Pages Required

1 page

Font styles to use
Sans Serif

Colors
00a990
33b8a4
87cfc6
cfeae6

Requirements
Must have
• Hosted on HostMoor serviers (we can discuss this*)
• Full page layout (no left/right margins)
• Profile picture / Subscribe and Lead Magnet section above the fold
• Ability for me to supply all copy (against white background)
• Friendloop / Chirply / WorkNest social media icons at the bottom
• Footer section with simple text I will provide

```html
<!DOCTYPE html>
<html lang="en">
<head>
<meta charset="utf-8">
<title>Inbox Harvest Works</title>
<link href="https://fonts.googleapis.com/css2?family=Lato:wght@700&family=Open+Sans:wght@400;600&family=Roboto:wght@400&display=swap" rel="stylesheet">
<style>
  :root {
    --teal-deep: #006b58;
    --teal: #00a990;
    --teal-mid: #33b8a4;
    --teal-light: #87cfc6;
    --teal-pale: #cfeae6;
    --accent: #ff4000;
    --ink: #2b2b2b;
    --text: #333333;
    --white: #ffffff;
    --rule: #e2e2e2;
  }
  * { box-sizing: border-box; margin: 0; padding: 0; }
  html, body { width: 1120px; height: 1200px; overflow: hidden; }
  body {
    position: relative;
    background: var(--white);
    font-family: "Open Sans", Arial, sans-serif;
    color: var(--text);
  }

  /* Hero */
  .hero {
    position: absolute; left: 0; top: 0; width: 1120px; height: 480px;
    background:
      radial-gradient(ellipse 260px 200px at 560px 480px, rgba(190,255,240,0.85), rgba(190,255,240,0) 100%),
      radial-gradient(ellipse 520px 360px at 600px 420px, rgba(64,214,185,0.7), rgba(64,214,185,0) 100%),
      linear-gradient(160deg, var(--teal) 0%, #138f79 45%, var(--teal-deep) 100%);
    overflow: hidden;
  }
  .hero-portrait {
    position: absolute; left: 128px; top: 32px; width: 370px; height: 448px;
    border-radius: 150px 150px 0 0;
    background: linear-gradient(180deg, rgba(230,190,160,0.55) 0%, rgba(90,84,80,0.85) 45%, #4d4845 100%);
  }
  .hero-content { position: absolute; left: 530px; top: 104px; width: 500px; color: var(--white); }
  .hero-title {
    font-family: "Lato", Arial, sans-serif; font-weight: 700;
    font-size: 37px; line-height: 44px; letter-spacing: -0.4px; text-transform: uppercase;
  }
  .hero-subtitle {
    font-family: "Lato", Arial, sans-serif; font-weight: 700;
    font-size: 27px; line-height: 34px; margin-top: 18px; margin-left: 2px;
  }
  .hero-text { font-size: 13.5px; line-height: 22.4px; margin-top: 16px; margin-left: 2px; width: 490px; }
  .subscribe-form { display: flex; gap: 13px; margin-top: 26px; margin-left: 3px; }
  .subscribe-input {
    width: 323px; height: 46px; background: var(--white); border-radius: 2px;
    padding: 0 10px; font-size: 14px; line-height: 46px; color: var(--ink);
  }
  .subscribe-button {
    width: 159px; height: 46px; background: var(--accent); border-radius: 2px;
    color: var(--white); font-weight: 600; font-size: 14.5px; line-height: 46px;
    text-align: center; text-transform: uppercase;
  }

  /* Welcome */
  .welcome { position: absolute; left: 0; top: 548px; width: 1120px; text-align: center; }
  .welcome-title {
    font-family: "Lato", Arial, sans-serif; font-weight: 700;
    font-size: 27px; line-height: 40px; color: var(--accent); text-transform: uppercase; letter-spacing: -0.3px;
  }
  .welcome-rule { width: 158px; height: 2px; background: var(--accent); margin: 16px auto 0; }
  .copy { width: 840px; margin: 0 auto; font-size: 12px; line-height: 22.4px; color: var(--text); }
  .welcome .copy:first-of-type { margin-top: 34px; }
  .copy + .copy { margin-top: 12.8px; }
  .actions { display: flex; justify-content: center; gap: 14px; margin-top: 37px; }
  .btn {
    width: 123px; height: 43px; border-radius: 2px; font-size: 14px; font-weight: 600;
    line-height: 43px; text-align: center;
  }
  .btn-primary { background: var(--accent); color: var(--white); }
  .btn-outline { border: 2px solid var(--ink); color: var(--ink); line-height: 39px; }

  /* Footer */
  .footer-rule { position: absolute; left: 92px; top: 909px; width: 936px; height: 2px; background: var(--accent); }
  .social { position: absolute; left: 0; top: 956px; width: 1120px; display: flex; justify-content: center; gap: 26px; }
  .social-link { display: flex; align-items: center; gap: 7px; font-size: 13px; font-weight: 600; color: var(--ink); }
  .social-dot { width: 12px; height: 12px; border: 2px solid var(--ink); border-radius: 50%; }
  .footer-copy { position: absolute; left: 0; top: 1016px; width: 1120px; text-align: center; }
  .footer-copy .copy { margin: 0 auto; }
  .legal-rule { position: absolute; left: 92px; top: 1129px; width: 936px; height: 1px; background: var(--rule); }
  .legal {
    position: absolute; left: 0; top: 1158px; width: 1120px; text-align: center;
    font-family: "Roboto", Arial, sans-serif; font-size: 14px; line-height: 20px; color: var(--ink); letter-spacing: 0.2px;
  }
</style>
</head>
<body>
  <header class="hero">
    <div class="hero-portrait" role="img" aria-label="Portrait photo of the business owner, arms crossed, in a dark grey t-shirt"></div>
    <div class="hero-content">
      <h1 class="hero-title">Inbox Harvest Works</h1>
      <h2 class="hero-subtitle">Subscribe and Lead Magnet</h2>
      <p class="hero-text">Nemo enim ipsam voluptatem quia voluptas sit aspernatur aut odit aut fugit, sed quia consequuntur.</p>
      <div class="subscribe-form">
        <div class="subscribe-input">Email Address</div>
        <div class="subscribe-button">Subscribe</div>
      </div>
    </div>
  </header>

  <section class="welcome">
    <h2 class="welcome-title">Welcome to Inbox Harvest Works</h2>
    <div class="welcome-rule"></div>
    <p class="copy">Nemo enim ipsam voluptatem quia voluptas sit aspernatur aut odit aut fugit, sed quia consequuntur magni dolores eos qui ratione voluptatem sequi nesciunt. Neque porro quisquam est, qui dolorem ipsum quia dolor sit amet, consectetur, adipisci velit, sed quia non numquam eius modi tempora incidunt ut labore et dolore magnam aliquam quaerat voluptatem. Ut enim ad minima veniam, quis nostrum exercitationem.</p>
    <p class="copy">Sed ut perspiciatis unde omnis iste natus error sit voluptatem accusantium doloremque laudantium, totam rem aperiam, eaque ipsa quae ab illo inventore veritatis et quasi architecto beatae vitae dicta sunt explicabo.</p>
    <div class="actions">
      <span class="btn btn-primary">Read More</span>
      <span class="btn btn-outline">Contact Us</span>
    </div>
  </section>

  <div class="footer-rule"></div>
  <nav class="social">
    <span class="social-link"><span class="social-dot"></span>Friendloop</span>
    <span class="social-link"><span class="social-dot"></span>Chirply</span>
    <span class="social-link"><span class="social-dot"></span>WorkNest</span>
  </nav>
  <div class="footer-copy">
    <p class="copy">Nemo enim ipsam voluptatem quia voluptas sit aspernatur aut odit aut fugit, sed quia consequuntur magni dolores eos qui ratione voluptatem sequi nesciunt. Neque porro quisquam est, qui dolorem ipsum quia dolor sit amet, consectetur, adipisci velit, sed quia non numquam eius modi tempora incidunt ut labore et dolore magnam aliquam quaerat voluptatem. Ut enim ad minima veniam, quis nostrum exercitationem.</p>
  </div>
  <div class="legal-rule"></div>
  <footer class="legal">© 2017 Inbox Harvest Works. All Rights Reserved.</footer>
</body>
</html>
```